TalkWell needs a Letterhead

We need a letterhead for our company "TalkWell Consultants". Logo is attached. The company color is Turquoise. Icons for website, scan logo for website, icons for address, e-mail and phone appreciated rather than just words.

```html
<!DOCTYPE html>
<html lang="en">
<head>
<meta charset="utf-8">
<title>TalkWell Consultants Letterhead</title>
<link href="https://fonts.googleapis.com/css2?family=Source+Sans+3:wght@400&display=swap" rel="stylesheet">
<style>
  :root {
    --brand-blue: #2f79c2;
    --brand-green: #8cc63f;
    --ink: #231f20;
    --rule: #9a9a9a;
    --paper: #ffffff;
  }
  * { margin: 0; padding: 0; box-sizing: border-box; }
  html, body {
    width: 850px; height: 1200px; overflow: hidden;
    background: var(--paper);
  }
  .letterhead {
    position: relative; width: 850px; height: 1200px; overflow: hidden;
    font-family: "Source Sans 3", "Myriad Pro", sans-serif;
    color: var(--ink);
  }
  .header-wave { position: absolute; top: 0; left: 0; width: 850px; height: 150px; }
  .brand {
    position: absolute; display: flex; align-items: center;
    color: var(--brand-blue); font-weight: 400;
  }
  .brand-mark { background: var(--brand-blue); flex: none; }
  .brand-name { line-height: 1; }
  .brand-sub { display: block; text-transform: uppercase; }

  .brand--header { left: 46px; top: 62px; gap: 22px; }
  .brand--header .brand-mark { width: 58px; height: 58px; }
  .brand--header .brand-name { font-size: 40px; }
  .brand--header .brand-sub { font-size: 16px; letter-spacing: 4.6px; margin-top: 4px; }

  .letter-body {
    position: absolute; left: 68px; top: 278px; width: 741px;
    font-size: 17px; line-height: 27.3px; text-align: justify;
  }
  .letter-body p + p { margin-top: 11.8px; }

  .footer {
    position: absolute; left: 0; top: 1078px; width: 850px; height: 115px;
  }
  .brand--footer { left: 35px; top: 18px; gap: 16px; }
  .brand--footer .brand-mark { width: 52px; height: 52px; }
  .brand--footer .brand-name { font-size: 31px; }
  .brand--footer .brand-sub { font-size: 13px; letter-spacing: 3.4px; margin-top: 3px; }
  .footer-rule {
    position: absolute; left: 300px; top: 2px; width: 2px; height: 112px;
    background: var(--rule);
  }
  .contact-list {
    position: absolute; left: 350px; top: 2px; list-style: none;
    font-size: 16px; line-height: 31px;
  }
  .contact-list li { display: flex; align-items: center; height: 30.6px; }
  .contact-icon { width: 24px; height: 24px; margin-right: 29px; flex: none; }
</style>
</head>
<body>
<div class="letterhead">
  <svg class="header-wave" viewBox="0 0 850 150" aria-hidden="true">
    <path fill="var(--brand-green)" d="M0,20 C130,12 270,24 420,68 C580,116 720,124 850,118 V146 C700,146 560,122 420,86 C260,44 120,24 0,24 Z"/>
    <path fill="var(--brand-blue)" d="M0,0 H850 V112 C720,120 590,112 440,70 C290,28 190,16 120,14 C80,13 40,16 0,19 Z"/>
    <path fill="#ffffff" opacity="0.18" d="M520,0 C560,40 620,70 700,90 L720,0 Z"/>
  </svg>

  <div class="brand brand--header">
    <span class="brand-mark"></span>
    <span class="brand-name">TalkWell<span class="brand-sub">Consultants</span></span>
  </div>

  <main class="letter-body">
    <p>Lorem ipsum dolor sit amet, sea ex scripta molestiae. No cum omnis congue, pro in augue civibus concludaturque, has habeo quando at. Cu his causae aliquid deserunt, dignissim neglegentur pri cu. Essent adolescens usu te, ut ullum graeco duo, vim ad meis adhuc. Inani delicatissimi at quo, nec et nullam prompta habemus. Hinc graeco perpetua quo te, meis habeo incorrupte eu nam.</p>
    <p>Quidam persecuti ut sed, maiorum propriae nec ex. Augue delenit tincidunt has id. Delicata salutandi vim ne, ea eam expetendis assueverit definitiones, has et labores facilisi deseruisse. Sale consequat assueverit per at. Omnes omnium lobortis te mea.</p>
    <p>His ubique animal molestie ut. Sit an nostro argumentum. Sit doming tritani saperet te. In omnesque similique vis, quaerendum persequeris eu sea. Soluta disputando ex mel, ea pri dicit perpetua dissentias. Ei mea nemore phaedrum scriptorem.Lorem ipsum dolor sit amet, sea ex scripta molestiae. No cum omnis congue, pro in augue civibus concludaturque, has habeo quando at. Cu his causae aliquid deserunt, dignissim neglegentur pri cu. Essent adolescens usu te, ut ullum graeco duo, vim ad meis adhuc. Inani delicatissimi at quo, nec et nullam prompta habemus. Hinc graeco perpetua quo te, meis habeo incorrupte eu nam.</p>
    <p>Quidam persecuti ut sed, maiorum propriae nec ex. Augue delenit tincidunt has id. Delicata salutandi vim ne, ea eam expetendis assueverit definitiones, has et labores facilisi deseruisse. Sale consequat assueverit per at. Omnes omnium lobortis te mea.</p>
    <p>His ubique animal molestie ut. Sit an nostro argumentum. Sit doming tritani saperet te. In omnesque similique vis, quaerendum persequeris eu sea. Soluta disputando ex mel, ea pri dicit perpetua dissentias. Ei mea nemore phaedrum scriptorem.His ubique animal molestie ut. Sit an nostro argumentum. Sit doming tritani saperet te. In omnesque similique vis, quaerendum persequeris eu sea. Soluta disputando ex mel, ea pri dicit perpetua dissentias. Ei mea nemore phaedrum scriptorem.</p>
  </main>

  <footer class="footer">
    <div class="brand brand--footer">
      <span class="brand-mark"></span>
      <span class="brand-name">TalkWell<span class="brand-sub">Consultants</span></span>
    </div>
    <div class="footer-rule"></div>
    <ul class="contact-list">
      <li>
        <svg class="contact-icon" viewBox="0 0 24 24" aria-label="Address">
          <path fill="var(--brand-green)" d="M12 2 L1 12 H4 V22 H10 V15 H14 V22 H20 V12 H23 Z M17 3 H20 V8 L17 5.5 Z"/>
        </svg>
        <span>Quidam persecuti ut sed, maiorum propriae nec ex</span>
      </li>
      <li>
        <svg class="contact-icon" viewBox="0 0 24 24" aria-label="Website">
          <circle cx="12" cy="12" r="10" fill="none" stroke="var(--brand-blue)" stroke-width="2"/>
          <ellipse cx="12" cy="12" rx="4.5" ry="10" fill="none" stroke="var(--brand-blue)" stroke-width="1.6"/>
          <rect x="1" y="9" width="22" height="6" fill="var(--brand-blue)"/>
          <path d="M3 5.5 H21 M3 18.5 H21" stroke="var(--brand-blue)" stroke-width="1.4"/>
        </svg>
        <span>www.loremipsum.com</span>
      </li>
      <li>
        <svg class="contact-icon" viewBox="0 0 24 24" aria-label="Email">
          <text x="12" y="19" text-anchor="middle" font-family="Source Sans 3, sans-serif" font-size="24" fill="var(--brand-green)">@</text>
        </svg>
        <span>loremipsum@lorem.com</span>
      </li>
      <li>
        <svg class="contact-icon" viewBox="0 0 24 24" aria-label="Phone">
          <rect x="7" y="2" width="12" height="20" rx="2" fill="var(--brand-blue)"/>
          <rect x="9" y="5" width="8" height="9" fill="#ffffff"/>
          <path d="M7 10 C4 11 4 17 7 18" fill="none" stroke="var(--brand-blue)" stroke-width="2"/>
        </svg>
        <span>#0000 000 000</span>
      </li>
    </ul>
  </footer>
</div>
</body>
</html>
```